Design for Bright Oak Homes real estate agency

Incorporate logo into new business cards. I need to include the Harlow Pemberton logo incorporated into Bright Oak Homes on one side of the card (attached). On the other side I see just the icon with "Merle Dunaway" (attached) with "Rooted in Care" either included as is or removed from logo and rather put as a tag line on the business card separate from the main logo. Contact information:

Merle Dunaway
Associate Broker
Cell: 555-307-1948
Email: merledunaway@brightoakhomes.example
Web: www.brightoakhomes.example

Target Market(s)

Buyers, Sellers, Builders and Investors of homes and land

Industry/Entity Type

Real Estate Agent

Contact Information for Business Card

My client base tend to be higher end home buyers, sellers, builders and investors. I have been more and more in land and subdivisions for builders and investors. The card should not be cluttered. Clean and simple - yet with an air of exclusive/high end

Colors

Designer to choose colors to be used in the design.

Requirements
Must have
• Must have the logo on one side that has Harlow Pemberton logo incorporated. The side that has my contact information does not have to have the Harlow Pemberton logo incorporated.
• Must include "Rooted in Care" tag line either within logo (as is) or removed from logo and included in another position on the side of the business card with contact information.
Should not have
• Should not have Harlow Pemberton logo incorporated into Bright Oak Homes logo on both sides of business card. Would like the Bright Oak Homes logo that has Harlow Logo only on the back side of card without contact information.

```html
<!DOCTYPE html>
<html lang="en">
<head>
<meta charset="utf-8">
<title>Bright Oak Homes – Business Card</title>
<link rel="stylesheet" href="https://fonts.googleapis.com/css2?family=Cinzel:wght@500&family=Sorts+Mill+Goudy&family=Roboto:wght@400;500&display=swap">
<style>
  :root {
    --backdrop: #e6e6e4;
    --paper: #f3f3f2;
    --walnut: #5a3b09;
    --gold: #c6a624;
    --gold-text: #c9a526;
    --white: #ffffff;
  }
  * { margin: 0; padding: 0; box-sizing: border-box; }
  html, body {
    width: 1200px; height: 960px; overflow: hidden;
    background: var(--backdrop);
  }
  .stage { position: relative; width: 1200px; height: 960px; }

  .card {
    position: absolute; width: 600px; height: 342px;
    border-radius: 22px; overflow: hidden;
  }

  /* Front */
  .card-front { left: 314px; top: 113px; background: var(--walnut); }
  .card-front .wave { position: absolute; left: 0; top: 0; }
  .brand-lockup {
    position: absolute; left: 124px; top: 52px;
    display: flex; align-items: center; gap: 18px;
  }
  .brand-mark { width: 64px; height: 64px; border-radius: 50%; background: var(--gold); }
  .brand-name {
    font-family: "Cinzel", serif; font-weight: 500;
    font-size: 25px; letter-spacing: 2px; color: var(--walnut); line-height: 1;
  }
  .brand-tagline {
    font-family: "Roboto", sans-serif; font-size: 9px;
    letter-spacing: 3.2px; color: var(--walnut); text-transform: uppercase;
    margin-top: 5px; text-align: center;
  }
  .agent {
    position: absolute; right: 346px; top: 245px; text-align: right;
    font-family: "Roboto", sans-serif; text-transform: uppercase;
  }
  .agent-name { font-size: 20px; font-weight: 500; color: var(--gold-text); line-height: 1.2; }
  .agent-title { font-size: 15px; color: var(--white); margin-top: 3px; }
  .divider {
    position: absolute; left: 279px; top: 228px; width: 2px; height: 80px;
    background: var(--white);
  }
  .contacts {
    position: absolute; left: 304px; top: 239px; list-style: none;
    font-family: "Roboto", sans-serif; font-size: 14px; color: var(--white);
  }
  .contacts li { display: flex; align-items: center; gap: 8px; height: 19.5px; }
  .contacts svg { width: 12px; height: 12px; fill: var(--gold-text); flex: none; }

  /* Back */
  .card-back { left: 312px; top: 472px; background: var(--gold); }
  .back-lockup {
    position: absolute; left: 106px; top: 118px;
    display: flex; align-items: center; gap: 14px; color: var(--walnut);
  }
  .back-mark { width: 70px; height: 70px; border-radius: 50%; background: var(--walnut); }
  .back-name {
    font-family: "Sorts Mill Goudy", serif; font-size: 32px; line-height: 1;
  }
  .back-sub { display: flex; align-items: center; gap: 10px; margin-top: 4px; }
  .back-agent { flex: 1; text-align: center; }
  .back-agent-name {
    font-family: "Cinzel", serif; font-size: 13px; letter-spacing: 2px;
    display: flex; align-items: center; gap: 6px;
  }
  .back-agent-name::before, .back-agent-name::after {
    content: ""; flex: 1; height: 1px; background: var(--walnut);
  }
  .back-tagline {
    font-family: "Roboto", sans-serif; font-size: 7px; letter-spacing: 2.6px;
    text-transform: uppercase;
  }
  .partner-name {
    font-family: "Roboto", sans-serif; font-size: 8px; font-weight: 500;
    line-height: 1.1; width: 50px;
  }
  .back-url {
    position: absolute; left: 0; right: 0; top: 286px; text-align: center;
    font-family: "Roboto", sans-serif; font-size: 14px; letter-spacing: 3px;
    color: var(--walnut);
  }
</style>
</head>
<body>
<main class="stage">
  <section class="card card-front">
    <svg class="wave" width="600" height="342" viewBox="0 0 600 342" aria-hidden="true">
      <path d="M0 0 H600 V125 C580 175 520 175 400 182 C300 188 200 200 120 180 C50 160 15 150 0 122 Z" fill="var(--paper)"/>
    </svg>
    <div class="brand-lockup">
      <div class="brand-mark"></div>
      <div>
        <div class="brand-name">MERLE DUNAWAY</div>
        <div class="brand-tagline">Rooted in Care</div>
      </div>
    </div>
    <div class="agent">
      <div class="agent-name">Merle Dunaway</div>
      <div class="agent-title">Associate Broker</div>
    </div>
    <div class="divider"></div>
    <ul class="contacts">
      <li><svg viewBox="0 0 12 12"><path d="M3 0h6a1 1 0 0 1 1 1v10a1 1 0 0 1-1 1H3a1 1 0 0 1-1-1V1a1 1 0 0 1 1-1zm.5 1.5v8h5v-8z"/></svg>555-307-1948</li>
      <li><svg viewBox="0 0 12 12"><path d="M0 2.5h12v7H0z M0 2.5l6 4 6-4" /></svg>merledunaway@brightoakhomes.example</li>
      <li><svg viewBox="0 0 12 12"><circle cx="6" cy="6" r="6"/></svg>www.brightoakhomes.example</li>
    </ul>
  </section>

  <section class="card card-back">
    <div class="back-lockup">
      <div class="back-mark"></div>
      <div>
        <div class="back-name">BrightOakHomes</div>
        <div class="back-sub">
          <div class="back-agent">
            <div class="back-agent-name">MERLE DUNAWAY</div>
            <div class="back-tagline">Rooted in Care</div>
          </div>
          <div class="partner-name">Harlow Pemberton</div>
        </div>
      </div>
    </div>
    <div class="back-url">www.brightoakhomes.example</div>
  </section>
</main>
</body>
</html>
```